Business cards and logo for Pellicott Law, P.A.

I need a business card and logo design for a new law firm in Miami, Florida called Pellicott Law, P.A. I, Dominic R. Pellicott, am the only lawyer in the firm. The law firm will mainly serve businesses but will also handle many other cases. Preferred colors are green and/or gray, but open minded to other suggestions.

Industry/Entity Type

Legal

Contact Information for Business Card

Phone Number TBD. Address is:
412 NE 19TH AVE STE 230
MIAMI, FL 33152

```html
<!DOCTYPE html>
<html lang="en">
<head>
<meta charset="utf-8">
<title>Pellicott Law, P.A. — Business Card</title>
<link rel="stylesheet" href="https://fonts.googleapis.com/css2?family=Libre+Baskerville&family=Lato:ital,wght@0,400;0,700;1,400&display=swap">
<style>
  :root {
    --backdrop: #2b2b2b;
    --card-light: #f4f4f4;
    --card-light-edge: #dcdcdc;
    --card-dark: #484848;
    --ink-dark: #2e2e2e;
    --ink-light: #f2f2f2;
    --ink-muted: #cfcfcf;
    --rule: #d9d9d9;
  }
  * { box-sizing: border-box; margin: 0; padding: 0; }
  html, body {
    width: 1200px; height: 873px; overflow: hidden;
    background: var(--backdrop);
  }
  .card {
    position: absolute; left: 180px; top: 196px;
    width: 840px; height: 480px;
    background: var(--card-dark);
    box-shadow: 0 12px 40px rgba(0,0,0,.45);
    overflow: hidden;
  }
  .card__header {
    height: 200px;
    background: linear-gradient(180deg, var(--card-light) 0%, var(--card-light-edge) 100%);
    display: flex; align-items: center; justify-content: flex-end;
    padding-right: 64px;
  }
  .firm-name {
    font-family: "Libre Baskerville", serif;
    font-size: 52px; font-weight: 400; color: var(--ink-dark);
    letter-spacing: .5px;
  }
  .card__stripes { height: 30px; position: relative; }
  .card__stripes::before, .card__stripes::after {
    content: ""; position: absolute; left: 0; right: 0; background: var(--rule);
  }
  .card__stripes::before { top: 8px; height: 3px; }
  .card__stripes::after { top: 17px; height: 2px; }
  .card__body {
    display: flex; align-items: center; height: 250px; padding-bottom: 30px;
  }
  .person {
    width: 470px; text-align: center;
    font-family: "Lato", sans-serif; color: var(--ink-light);
  }
  .person__name { font-size: 23px; font-weight: 700; }
  .person__title { font-size: 16px; font-style: italic; color: var(--ink-muted); margin-top: 2px; }
  .person__address { font-size: 18px; color: var(--ink-muted); margin-top: 26px; line-height: 1.45; }
  .divider { width: 2px; height: 140px; background: var(--rule); }
  .contact {
    list-style: none; padding-left: 48px;
    font-family: "Lato", sans-serif; font-size: 18px; color: var(--ink-light);
  }
  .contact__item { display: flex; align-items: center; gap: 14px; margin: 10px 0; }
  .contact__icon { width: 20px; height: 20px; flex: none; }
</style>
</head>
<body>
  <main class="card">
    <header class="card__header">
      <h1 class="firm-name">Pellicott Law, P.A.</h1>
    </header>
    <div class="card__stripes"></div>
    <section class="card__body">
      <div class="person">
        <p class="person__name">Dominic R. Pellicott</p>
        <p class="person__title">Lawyer</p>
        <p class="person__address">412 NE 19th Ave, Suite 230<br>Miami, Florida 33152</p>
      </div>
      <div class="divider"></div>
      <ul class="contact">
        <li class="contact__item">
          <svg class="contact__icon" viewBox="0 0 20 20" fill="none" stroke="#f2f2f2" stroke-width="1.6"><rect x="5" y="1.5" width="10" height="17" rx="2"/><line x1="9" y1="15.5" x2="11" y2="15.5"/></svg>
          (305) 555-0142
        </li>
        <li class="contact__item">
          <svg class="contact__icon" viewBox="0 0 20 20" fill="#f2f2f2"><path d="M2 5h16v10H2z"/><path d="M2 5l8 6 8-6" fill="none" stroke="#484848" stroke-width="1.4"/></svg>
          dominic@pellicottlegal.com
        </li>
        <li class="contact__item">
          <svg class="contact__icon" viewBox="0 0 20 20" fill="none" stroke="#f2f2f2" stroke-width="1.8" stroke-linecap="round"><path d="M8.5 11.5l3-3"/><path d="M9.5 6.5l1.8-1.8a3 3 0 0 1 4.2 4.2l-1.8 1.8"/><path d="M10.5 13.5l-1.8 1.8a3 3 0 0 1-4.2-4.2l1.8-1.8"/></svg>
          www.pellicottlegal.com
        </li>
      </ul>
    </section>
  </main>
</body>
</html>
```